Plakate für ein Juwelier Geschäft
Zielgruppe
Juwelier Geschäft mit Gold, Silber, Diamanten und Trauringe. Zielgruppe Schmuck Interessierte, besonders individuelle Trauringberatung mit Konfiguration für junge Paare mit 20 % Rabatt
Aufgabenstellung
2 Bilder: Auf dem ersten Bild Goldschmuck mit Kette, Ring und Ohrringe bei einer jungen Dame und beim zweiten Bild ein junges Paar mit Trauringen. Spruch ist erwünscht. Name, Logo und Adresse vom Laden wird später ergänzt. Bitte kostenlose bzw, lizenzfreie Bilder verwenden. Plakat wird digital benutzt, Auflösung 576 x 408 Pixel, Schrifthöhe 30 Pixel und 50 Pixel

```html
<!DOCTYPE html>
<html lang="de">
<head>
<meta charset="utf-8">
<title>Goldhafen – Juwelier Plakat</title>
<link rel="stylesheet" href="https://fonts.googleapis.com/css2?family=Bebas+Neue&family=Montserrat:wght@600;800&display=swap">
<style>
  :root {
    --page: #cbcbcb;
    --bark: #3a302c;
    --bark-deep: #2a2320;
    --olive: #6b6232;
    --gold: #d9a21c;
    --gold-light: #f1d98a;
    --gold-dark: #8a5a1e;
    --white: #ffffff;
    --icon: #f2c21a;
  }
  html, body {
    margin: 0;
    width: 1200px;
    height: 1117px;
    overflow: hidden;
    background: var(--page);
  }
  .poster {
    position: absolute;
    left: 75px;
    top: 187px;
    width: 1050px;
    height: 743px;
    overflow: hidden;
    background:
      radial-gradient(ellipse at 10% 10%, rgba(107,98,50,.55), transparent 55%),
      radial-gradient(ellipse at 80% 100%, rgba(107,98,50,.6), transparent 50%),
      var(--bark);
  }
  .poster-shapes {
    position: absolute;
    inset: 0;
  }
  .brand {
    position: absolute;
    left: 67px;
    top: 78px;
    margin: 0;
    font-family: "Montserrat", sans-serif;
    font-weight: 800;
    font-size: 50px;
    letter-spacing: 1px;
    color: var(--gold);
  }
  .headline {
    position: absolute;
    left: 67px;
    top: 192px;
    margin: 0;
    font-family: "Bebas Neue", sans-serif;
    font-weight: 400;
    font-size: 57px;
    line-height: 51px;
    color: var(--white);
  }
  .intro {
    position: absolute;
    left: 64px;
    top: 540px;
    width: 280px;
    margin: 0;
    font-family: "Montserrat", sans-serif;
    font-weight: 600;
    font-size: 15px;
    line-height: 20px;
    color: var(--white);
  }
  .contact {
    position: absolute;
    left: 64px;
    top: 640px;
    margin: 0;
    padding: 0;
    list-style: none;
    font-family: "Montserrat", sans-serif;
    font-weight: 800;
    font-size: 22px;
    color: var(--white);
  }
  .contact li {
    display: flex;
    align-items: center;
    height: 35px;
  }
  .contact svg {
    width: 22px;
    height: 22px;
    margin-right: 19px;
    flex: none;
  }
</style>
</head>
<body>
  <main class="poster">
    <svg class="poster-shapes" viewBox="0 0 1050 743" width="1050" height="743">
      <defs>
        <linearGradient id="photoFade" x1="0" x2="1" y1="0" y2="0">
          <stop offset="0" stop-color="#1e1a1c" stop-opacity="0"/>
          <stop offset="0.18" stop-color="#1e1a1c"/>
          <stop offset="0.45" stop-color="#4f7e9c"/>
          <stop offset="0.7" stop-color="#9a7434"/>
          <stop offset="1" stop-color="#7fa9c2"/>
        </linearGradient>
        <linearGradient id="goldBand" x1="0" x2="1" y1="0" y2="0">
          <stop offset="0" stop-color="var(--gold-dark)"/>
          <stop offset="0.45" stop-color="var(--gold-light)"/>
          <stop offset="0.8" stop-color="var(--gold)"/>
          <stop offset="1" stop-color="var(--gold-dark)"/>
        </linearGradient>
        <radialGradient id="coupleTone" cx="0.45" cy="0.5" r="0.6">
          <stop offset="0" stop-color="#d9b49a"/>
          <stop offset="0.55" stop-color="#7e8ea4"/>
          <stop offset="1" stop-color="#2c3550"/>
        </radialGradient>
      </defs>

      <path class="photo-woman" role="img" aria-label="Foto: junge Dame in blauem Gewand mit Goldkette, Ring und Ohrringen"
            d="M330,0 H1050 V440 C990,560 820,615 610,600 L330,600 Z" fill="url(#photoFade)"/>

      <path class="band-gold-left" d="M0,426 C120,408 250,428 340,468 L340,484 C250,450 120,444 0,470 Z" fill="url(#goldBand)"/>
      <path class="band-white-left" d="M0,482 C130,456 260,474 340,512 L340,530 C250,492 120,488 0,510 Z" fill="var(--white)"/>

      <path class="band-gold-right" d="M1050,430 C990,565 820,622 600,598 L600,616 C830,640 1000,585 1050,478 Z" fill="url(#goldBand)"/>
      <path class="band-white-right" d="M1050,505 C985,610 820,650 600,625 C700,660 760,700 800,703 C720,712 660,690 560,640 C780,668 990,620 1050,540 Z" fill="var(--white)"/>

      <circle class="badge-frame" cx="483" cy="504" r="151" fill="var(--bark-deep)"/>
      <circle class="badge-ring" cx="483" cy="504" r="138" fill="url(#goldBand)"/>
      <circle class="photo-couple" role="img" aria-label="Foto: junges Paar mit Trauringen, Hände ineinander verhakt"
              cx="483" cy="504" r="131" fill="url(#coupleTone)"/>
    </svg>

    <p class="brand">Goldhafen</p>

    <h1 class="headline">Juwelier Geschäft<br>mit Gold, Silber,<br>Diamanten und<br>Trauringe.</h1>

    <p class="intro">Lorem ipsum dolor sit amet, consectetur adipiscing elit sed do eiusmod tempor incididunt ut labore et dolore magna.</p>

    <ul class="contact">
      <li>
        <svg viewBox="0 0 24 24" aria-hidden="true">
          <circle cx="12" cy="12" r="11" fill="var(--icon)"/>
          <g fill="none" stroke="var(--bark)" stroke-width="1.4">
            <circle cx="12" cy="12" r="6.5"/>
            <ellipse cx="12" cy="12" rx="3" ry="6.5"/>
            <line x1="5.5" y1="12" x2="18.5" y2="12"/>
          </g>
        </svg>
        GOLDHAFEN-SCHMUCK.EXAMPLE
      </li>
      <li>
        <svg viewBox="0 0 24 24" aria-hidden="true">
          <circle cx="12" cy="12" r="11" fill="var(--icon)"/>
          <path d="M12,5.5 a4.5,4.5 0 0 1 4.5,4.5 c0,3.3 -4.5,8 -4.5,8 s-4.5,-4.7 -4.5,-8 a4.5,4.5 0 0 1 4.5,-4.5 z" fill="var(--bark)"/>
          <circle cx="12" cy="10" r="1.7" fill="var(--icon)"/>
        </svg>
        48 LINDENWEG NORD, 20417
      </li>
    </ul>
  </main>
</body>
</html>
```